Cardiology practice business card

We need a business card for our cardiology practice "Bellmoor Cardiology". We have a new logo, attached below. We like the colours in the logo - red and charcoal. The front of the business card will need to have the doctors name, address, phone number and email. The back will need to have space to write 2 appointment dates and times.

```html
<!DOCTYPE html>
<html lang="en">
<head>
<meta charset="utf-8">
<title>Bellmoor Cardiology Business Card</title>
<link href="https://fonts.googleapis.com/css2?family=Montserrat:wght@400;500;600;700&family=Open+Sans:wght@400;600&display=swap" rel="stylesheet">
<style>
  :root {
    --red: #c8161d;
    --red-dark: #a50f15;
    --charcoal: #3a3a3c;
    --grey: #6b6b6e;
    --rule: #9a9a9a;
    --paper: #ffffff;
    --backdrop: #2a2b2d;
  }
  * { box-sizing: border-box; margin: 0; padding: 0; }
  html, body { width: 1200px; height: 874px; overflow: hidden; }
  body {
    background: var(--backdrop);
    font-family: "Open Sans", Arial, sans-serif;
    position: relative;
  }
  .card {
    position: absolute;
    left: 270px;
    width: 660px;
    height: 377px;
    background: var(--paper);
    border-radius: 22px;
    overflow: hidden;
    box-shadow: 0 10px 30px rgba(0,0,0,.45);
  }
  .card--back { top: 40px; }
  .card--front { top: 457px; }

  .brand {
    position: absolute;
    display: flex;
    align-items: center;
    gap: 10px;
    font-family: "Montserrat", Arial, sans-serif;
    font-weight: 700;
    color: var(--red);
    letter-spacing: .5px;
    white-space: nowrap;
  }
  .brand__dot {
    background: var(--red);
    border-radius: 50%;
    flex: none;
  }
  .card--back .brand { top: 34px; left: 34px; font-size: 21px; }
  .card--back .brand__dot { width: 14px; height: 14px; }

  .appointment__title {
    position: absolute;
    top: 92px; right: 40px;
    font-family: "Montserrat", Arial, sans-serif;
    font-weight: 600;
    font-size: 27px;
    color: var(--red);
  }
  .appointment__row {
    position: absolute;
    left: 34px; right: 40px;
    display: flex;
    align-items: flex-end;
    font-size: 15px;
    color: var(--red);
  }
  .appointment__row--one { top: 150px; }
  .appointment__row--two { top: 212px; }
  .appointment__label { white-space: nowrap; margin-right: 6px; }
  .appointment__line {
    flex: 1;
    border-bottom: 1.5px dotted var(--charcoal);
    margin-bottom: 4px;
    margin-right: 14px;
  }
  .appointment__line:last-of-type { margin-right: 6px; }
  .appointment__line--date { flex: 1.6; }
  .appointment__ampm { white-space: nowrap; }

  .band {
    position: absolute;
    left: 0; right: 0; top: 292px;
    height: 34px;
    background: linear-gradient(90deg, var(--red-dark), var(--red) 50%, var(--red-dark));
    display: flex; align-items: center; justify-content: center;
    color: #fff;
    font-size: 14px;
    letter-spacing: 3px;
  }
  .notice {
    position: absolute;
    top: 338px; left: 0; right: 0;
    text-align: center;
    font-size: 13px;
    letter-spacing: .6px;
    color: var(--grey);
  }

  .card--front .brand {
    top: 142px; left: 64px;
    font-size: 32px;
    line-height: 1.1;
    gap: 14px;
  }
  .card--front .brand__dot { width: 18px; height: 18px; }
  .brand__name { display: block; }
  .divider {
    position: absolute;
    left: 340px; top: 110px;
    width: 1.5px; height: 160px;
    background: linear-gradient(var(--rule), rgba(154,154,154,.2));
  }
  .contact {
    position: absolute;
    left: 372px; top: 118px;
    color: var(--charcoal);
  }
  .contact__name {
    font-family: "Montserrat", Arial, sans-serif;
    font-weight: 700;
    font-size: 27px;
    color: var(--red);
    margin-bottom: 18px;
  }
  .contact__address { font-size: 16px; line-height: 1.3; margin-bottom: 10px; }
  .contact__item {
    display: flex; align-items: center; gap: 10px;
    font-size: 16px; line-height: 1.35;
  }
  .contact__icon { width: 14px; height: 14px; flex: none; }
  .contact__icon--phone { fill: var(--red); }
  .contact__icon--mail { fill: none; stroke: var(--red); stroke-width: 2.4; stroke-linejoin: round; }
</style>
</head>
<body>

<section class="card card--back">
  <div class="brand"><span class="brand__dot"></span>Bellmoor Cardiology</div>
  <h2 class="appointment__title">Next Appointment</h2>

  <div class="appointment__row appointment__row--one">
    <span class="appointment__label">Date :</span><span class="appointment__line appointment__line--date"></span>
    <span class="appointment__label">Time :</span><span class="appointment__line"></span>
    <span class="appointment__ampm">AM/PM</span>
  </div>
  <div class="appointment__row appointment__row--two">
    <span class="appointment__label">Date :</span><span class="appointment__line appointment__line--date"></span>
    <span class="appointment__label">Time :</span><span class="appointment__line"></span>
    <span class="appointment__ampm">AM/PM</span>
  </div>

  <div class="band">www.bellmoor.com</div>
  <p class="notice">Please give 24 hours notice cancelling your appointment or a fee may be charged</p>
</section>

<section class="card card--front">
  <div class="brand">
    <span class="brand__dot"></span>
    <span><span class="brand__name">Bellmoor</span><span class="brand__name">Cardiology</span></span>
  </div>
  <div class="divider"></div>
  <div class="contact">
    <h1 class="contact__name">Daniel Ward</h1>
    <p class="contact__address">4120 Alder Crescent<br>Northfield, Canada 58213</p>
    <p class="contact__item">
      <svg class="contact__icon contact__icon--phone" viewBox="0 0 24 24" aria-hidden="true"><path d="M6.6 10.8a15.1 15.1 0 0 0 6.6 6.6l2.2-2.2a1 1 0 0 1 1-.25 11.4 11.4 0 0 0 3.6.57 1 1 0 0 1 1 1V20a1 1 0 0 1-1 1A17 17 0 0 1 3 4a1 1 0 0 1 1-1h3.5a1 1 0 0 1 1 1c0 1.25.2 2.45.57 3.57a1 1 0 0 1-.25 1z"/></svg>
      555-218-4630
    </p>
    <p class="contact__item">
      <svg class="contact__icon contact__icon--mail" viewBox="0 0 24 24" aria-hidden="true"><rect x="2.5" y="5" width="19" height="14"/><path d="M2.5 5l9.5 8 9.5-8"/></svg>
      info@bellmoor.com
    </p>
  </div>
</section>

</body>
</html>
```